Business card for consulting firm

We need a double-sided business card for consulting firm, VantorQ. The card should be professional but also creative and visually interesting.

Target Market(s)

Engineering and technology; transport industries; safety critical / heavy industry.

Contact Information for Business Card

See attached file with details.

Font styles to use
Sans Serif

```html
<!DOCTYPE html>
<html lang="en">
<head>
<meta charset="utf-8">
<title>VantorQ Business Card</title>
<link rel="stylesheet" href="https://fonts.googleapis.com/css2?family=Open+Sans:wght@400;600;700&display=swap">
<style>
  :root {
    --page-bg: #050505;
    --card-bg: #2a2a2a;
    --ink: #ffffff;
    --ink-soft: #e6e6e6;
  }
  * { box-sizing: border-box; margin: 0; padding: 0; }
  html, body {
    width: 1200px;
    height: 900px;
    overflow: hidden;
    background: var(--page-bg);
    font-family: "Open Sans", sans-serif;
    color: var(--ink);
  }
  .canvas {
    width: 1200px;
    height: 900px;
    display: flex;
    flex-direction: column;
    align-items: center;
    justify-content: center;
    gap: 56px;
  }
  .card {
    width: 620px;
    height: 354px;
    background: var(--card-bg);
    border-radius: 30px;
    position: relative;
  }
  .wordmark {
    display: inline-flex;
    flex-direction: column;
    align-items: flex-end;
    line-height: 1;
  }
  .wordmark__name {
    font-weight: 700;
    letter-spacing: 1px;
    color: var(--ink);
  }
  .wordmark__tagline {
    font-weight: 600;
    color: var(--ink);
  }
  .card--front {
    display: flex;
    align-items: center;
    justify-content: center;
  }
  .card--front .wordmark__name { font-size: 76px; }
  .card--front .wordmark__tagline { font-size: 21px; margin-top: 4px; }

  .card--back { padding: 58px 0 0 66px; }
  .card--back .wordmark__name { font-size: 58px; }
  .card--back .wordmark__tagline { font-size: 17px; margin-top: 3px; }

  .person { margin: 22px 0 0 134px; line-height: 1.25; }
  .person__name { font-size: 17px; font-weight: 700; letter-spacing: 0.3px; }
  .person__credentials, .person__role { font-size: 13px; color: var(--ink-soft); }

  .contact-list {
    list-style: none;
    margin: 14px 0 0 134px;
    font-size: 15px;
    line-height: 1.38;
  }
  .contact-list li { display: flex; align-items: center; gap: 7px; }
  .contact-list svg { width: 12px; height: 12px; flex: none; fill: var(--ink); }
</style>
</head>
<body>
<main class="canvas">
  <section class="card card--front" aria-label="Card front">
    <div class="wordmark">
      <span class="wordmark__name">VantorQ</span>
      <span class="wordmark__tagline">Safety &amp; Human Factors</span>
    </div>
  </section>

  <section class="card card--back" aria-label="Card back">
    <div class="wordmark">
      <span class="wordmark__name">VantorQ</span>
      <span class="wordmark__tagline">Safety &amp; Human Factors</span>
    </div>
    <div class="person">
      <p class="person__name">HELENA MARWICK</p>
      <p class="person__credentials">BA (Hons), M Psych Org, M Tech Mgt (HF)</p>
      <p class="person__role">Managing Director</p>
    </div>
    <ul class="contact-list">
      <li>
        <svg viewBox="0 0 12 12" aria-hidden="true"><path d="M1 4c0-1.5 2-2.5 5-2.5S11 2.5 11 4v1H8.5V3.8h-5V5H1z"/><rect x="2.5" y="6" width="7" height="5" rx="1"/></svg>
        +61 (0)400 555 018
      </li>
      <li>
        <svg viewBox="0 0 12 12" aria-hidden="true"><path d="M1 2.5h10v7H1z M1.6 3.1 6 6.6l4.4-3.5" fill="none" stroke="#fff" stroke-width="1.2"/></svg>
        hmarwick@vantorq.global
      </li>
      <li>
        <svg viewBox="0 0 12 12" aria-hidden="true"><circle cx="6" cy="6" r="5.5"/></svg>
        www.vantorq.com.au
      </li>
      <li>
        <svg viewBox="0 0 12 12" aria-hidden="true"><circle cx="6" cy="6" r="5.5"/></svg>
        www.vantorq.com.au
      </li>
    </ul>
  </section>
</main>
</body>
</html>
```